EPC Marketing Flyer Pinefold HC

Company Name: Pinefold Homecheck Ltd
Product: Residential EPCs
Territory: Nationwide (UK)
Marketing channel: Flyer will be used for email and postal mailshots. We have not targeted this particular segment of the market before, so we need it to be eye catching, clearly messaged and encourage the recipient to get in touch.

We need a flyer to promote our services to conduct EPCs owned by public and private sector for residential ONLY (NOT Commercial), on a large or small scale.

Our Surveyors: experienced and accredited surveyors, quality service, quick and professional

Our Business: Warm Ledger Accredited, Reputation in business for excellence, fast growing

Our Service: Friendly, high quality, quick and professional

Colours: Designs in green and white (same shade as corporate colours), with our logo, and warm ledger accreditation logo, promoting our business.

Target Market(s)

Estate Agencies, Housing Associations, Local Authorities (Housing Departments), House Builders (NOT Home Owners Directly)

Industry/Entity Type

It Company

Font styles to use
Sans Serif
Other font styles liked:
• Calibri

Colors
add136
9bcb3c
cadf82
f6faec
eaf2ce

Requirements
Must have
• Our contact number etc must be clearly visible, and that we do EPCs
• Must state: What is an EPC? An EPC (Energy Performance Certificate) gives a property an energy efficiency rating from A (most efficient) to G (least efficient) and is valid for 10 years. An EPC can also provide recommendations on home improvement measures which once complete can improve the energy efficiency of the property.
• Who needs and EPC? All landlords and home owners, as all properties available to buy or rent require a valid and current EPC.
• Contact details:
• Tel: 08000 915 462
• Website: www.pinefold-hc.co.uk
• Email: epc@pinefold-hc.co.uk
• we must also be ably to print out the flyer
Nice to have
• Nice images to accompany the text which give a feeling of Environmentally Green, Home Energy Efficiency, Home Warmth and family - see example attached. And image of survey professional at work.
Should not have
• Any reference to cost or pricing
• Warm ledger logo art work must not be any other size that that specified in guidance document attached.

```html
<!DOCTYPE html>
<html lang="en">
<head>
<meta charset="utf-8">
<title>Pinefold Homecheck Ltd – EPC Flyer</title>
<link rel="stylesheet" href="https://fonts.googleapis.com/css2?family=Oswald:wght@500&family=Open+Sans:wght@400;600;700&display=swap">
<style>
  :root {
    --brand-green: #7dbb2a;
    --brand-green-dark: #5e9a1c;
    --brand-lime: #9bcb3c;
    --brand-pale: #cadf82;
    --brand-mist: #eaf2ce;
    --brand-wash: #f6faec;
    --hero-tone: #a9c8e4;
    --ink: #3a3a3a;
    --ink-soft: #555;
    --white: #ffffff;
  }
  * { margin: 0; padding: 0; box-sizing: border-box; }
  html, body { width: 900px; height: 1200px; overflow: hidden; background: var(--white); }
  .flyer {
    position: relative;
    width: 900px;
    height: 1200px;
    overflow: hidden;
    background: linear-gradient(180deg, #fff 0%, #f3f3f3 55%, #fafafa 100%);
    font-family: "Open Sans", Calibri, sans-serif;
    color: var(--ink-soft);
  }
  .flyer__art { position: absolute; left: 0; top: 0; }
  .backdrop-wash {
    position: absolute;
    left: 0; top: 560px;
    width: 900px; height: 420px;
    background: radial-gradient(ellipse at 60% 45%, rgba(200,200,200,0.45), rgba(240,240,240,0) 70%);
  }
  .headline { position: absolute; left: 40px; top: 654px; width: 820px; }
  .headline__sub {
    font-weight: 700;
    font-size: 36px;
    line-height: 1.2;
    color: var(--ink);
    white-space: nowrap;
  }
  .info { position: absolute; top: 742px; }
  .info--what { left: 45px; width: 410px; }
  .info--who { left: 474px; width: 385px; }
  .info__heading {
    font-weight: 700;
    font-size: 23px;
    color: var(--brand-green-dark);
    margin-bottom: 8px;
  }
  .info__body {
    font-size: 15px;
    line-height: 1.5;
    text-align: justify;
    color: var(--ink-soft);
  }
  .accreditation {
    position: absolute;
    left: 478px; top: 868px;
    display: flex; align-items: center; gap: 16px;
  }
  .accreditation__badge {
    width: 44px; height: 50px;
    background: var(--brand-green);
    border-radius: 4px;
  }
  .accreditation__text {
    font-family: "Oswald", sans-serif;
    font-weight: 500;
    font-size: 23px;
    line-height: 1.15;
    color: var(--ink);
    text-transform: uppercase;
  }
  .contact {
    position: absolute;
    left: 227px; top: 971px;
    width: 466px; height: 100px;
    border-radius: 20px;
    background: var(--brand-green-dark);
    box-shadow: 0 4px 10px rgba(0,0,0,0.25);
    color: var(--white);
    text-align: center;
    overflow: hidden;
  }
  .contact__phone {
    display: flex; align-items: center; justify-content: center; gap: 14px;
    height: 62px;
    background: linear-gradient(180deg, #7cbd2e, #5e9a1c);
    font-weight: 700; font-size: 44px; letter-spacing: 0.5px;
  }
  .contact__icon { width: 32px; height: 32px; }
  .contact__email {
    border-top: 1px solid rgba(255,255,255,0.45);
    padding-top: 6px;
    font-weight: 600; font-size: 20px;
  }
  .brand {
    position: absolute; left: 50px; top: 1120px;
    display: flex; align-items: center; gap: 12px;
    color: var(--white);
    font-weight: 600; font-size: 24px;
  }
  .brand__dot { width: 40px; height: 40px; border-radius: 50%; background: var(--white); }
  .web {
    position: absolute; right: 40px; top: 1122px;
    display: flex; align-items: center; gap: 8px;
    padding: 8px 18px 8px 22px;
    border-radius: 22px;
    background: var(--white);
    font-weight: 700; font-size: 19px; color: var(--ink);
  }
  .web__globe { width: 16px; height: 16px; }
</style>
</head>
<body>
<main class="flyer">
  <svg class="flyer__art" width="900" height="1200" viewBox="0 0 900 1200">
    <defs>
      <linearGradient id="hero-fill" x1="0" y1="0" x2="0" y2="1">
        <stop offset="0" stop-color="#9fc2e4"/>
        <stop offset="1" stop-color="#b8d3ea"/>
      </linearGradient>
      <linearGradient id="band-green" x1="0" y1="0" x2="1" y2="0">
        <stop offset="0" stop-color="#8cc63a"/>
        <stop offset="1" stop-color="#add136"/>
      </linearGradient>
    </defs>

    <path class="band band--top" d="M0,0 H900 V150 C650,70 300,80 0,250 Z" fill="url(#band-green)"/>
    <path class="band band--top-stripe" d="M0,250 C300,80 650,70 900,150 V175 C650,100 300,110 0,275 Z" fill="var(--brand-pale)"/>

    <path class="hero" role="img" aria-label="Photo of a smiling family lying on grass under a blue sky beside a green house symbol"
          d="M0,275 C300,110 650,100 900,175 V395 C620,520 300,560 0,470 Z" fill="url(#hero-fill)"/>

    <path class="band band--hero-swoosh" d="M0,470 C300,560 620,520 900,395 V430 C640,560 300,600 0,520 Z" fill="url(#band-green)"/>
    <path class="band band--hero-stripe" d="M0,520 C300,600 640,560 900,430 V450 C640,585 300,620 0,545 Z" fill="var(--brand-mist)"/>

    <path class="band band--bottom-stripe" d="M0,1010 C300,1120 650,1090 900,960 V1200 H0 Z" fill="var(--brand-mist)"/>
    <path class="band band--bottom" d="M0,1045 C300,1150 650,1120 900,990 V1200 H0 Z" fill="url(#band-green)"/>

    <text class="headline__title" x="450" y="648" text-anchor="middle" textLength="820" lengthAdjust="spacingAndGlyphs"
          font-family="Oswald, sans-serif" font-weight="500" font-size="62" fill="var(--brand-green-dark)">EXPERIENCED AND ACCREDITED SURVEYORS</text>
  </svg>

  <div class="backdrop-wash" role="img" aria-label="Faded photo of a house behind the text"></div>

  <header class="headline">
    <p class="headline__sub">QUALITY SERVICE, QUICK AND PROFESSIONAL</p>
  </header>

  <section class="info info--what">
    <h2 class="info__heading">WHAT IS AN EPC?</h2>
    <p class="info__body">An EPC (Energy Performance Certificate) gives a property an energy efficiency rating from A (most efficient) to G (least efficient) and is valid for 10 years. An EPC can also provide recommendations on home improvement measures which once complete can improve the energy efficiency of the property.</p>
  </section>

  <section class="info info--who">
    <h2 class="info__heading">WHO NEEDS AND EPC?</h2>
    <p class="info__body">All landlords and home owners, as all properties available to buy or rent require a valid and current EPC.</p>
  </section>

  <div class="accreditation">
    <div class="accreditation__badge" role="img" aria-label="Warm Ledger accreditation badge"></div>
    <p class="accreditation__text">Reputation in business for<br>excellence, fast growing</p>
  </div>

  <div class="contact">
    <div class="contact__phone">
      <svg class="contact__icon" viewBox="0 0 32 32" aria-hidden="true">
        <rect x="1" y="1" width="30" height="30" rx="6" fill="#fff"/>
        <path d="M11 7c1 0 2 3 2.5 4.5.3 1-1.5 2-1.2 3 .8 2 2.5 3.7 4.5 4.5 1 .3 2-1.5 3-1.2 1.5.5 4.5 1.5 4.5 2.5 0 2-2 4-4 4C14 24.3 7.7 18 7.7 11 7.7 9 9 7 11 7z" fill="var(--brand-green-dark)"/>
      </svg>
      <span>08000 915 462</span>
    </div>
    <p class="contact__email">epc@pinefold-hc.co.uk</p>
  </div>

  <div class="brand">
    <span class="brand__dot"></span>
    <span class="brand__name">Pinefold Homecheck Ltd</span>
  </div>

  <div class="web">
    <span>www.pinefold-hc.co.uk</span>
    <svg class="web__globe" viewBox="0 0 16 16" aria-hidden="true">
      <circle cx="8" cy="8" r="7" fill="none" stroke="var(--brand-green)" stroke-width="1.4"/>
      <ellipse cx="8" cy="8" rx="3" ry="7" fill="none" stroke="var(--brand-green)" stroke-width="1.2"/>
      <path d="M1 8h14M2.5 4.5h11M2.5 11.5h11" stroke="var(--brand-green)" stroke-width="1.1"/>
    </svg>
  </div>
</main>
</body>
</html>
```